"Parcel Sheet Studio" Vendora Add-on Market Banner

Hey Designers! I need a photoshop banner to feature our web application, for use in the Vendora Add-on Market. See http://addons.vendora-example.com for examples of the other apps and their designs.
The image should be 310px wide x 100px tall. Suggested colors should be taken from our homepage: http://store.parcelsheetstudio-example.com/ and are also suggested below.
At minimum, the app banner must contain the name "Parcel Sheet Studio".
The application itself provides people with printable customized Invoice, Packing Slips templates, so imagery should reflect that in some way. Perhaps a printer or document icon for imagery.
I prefer flat design, or simple design without too much clutter or small details.
Target Market(s)
Adults based in United States, UK and Australia.. aged 25-35 who run online e-commerce businesses through Vendora.com
Industry/Entity Type
Printer
Requirements
Must have
- The words "Parcel Sheet Studio".
Black background, grey and white details.
Nice to have
- illustration style images, in flat design style if possible.
I like this type of design style: http://boxlayerweb-example.com/tour/overview/
Should not have
- Photo like images.
White background.

```html
<!DOCTYPE html>
<html lang="en">
<head>
<meta charset="utf-8">
<title>Parcel Sheet Studio — Vendora Add-on Market Banner</title>
<link rel="stylesheet" href="https://fonts.googleapis.com/css2?family=PT+Sans:wght@400;700&display=swap">
<style>
  :root {
    --page: #ffffff;
    --sun-yellow: #f6ca2c;
    --sun-orange: #f5a623;
    --sun-orange-soft: #f7b62a;
    --ink-teal: #1d6787;
    --sky-blue: #4b9bd6;
    --sky-teal: #2a93a2;
    --sky-mid: #3d97c4;
    --night-slate: #3a4b5e;
    --night-deep: #222b36;
    --night-mid: #2e3a48;
    --label-white: #ffffff;
    --sub-sky: #d6ecfa;
    --sub-night: #c5d0dc;
    --art-printer: #2f8fc4;
    --art-printer-warm: #f5a623;
  }
  * { margin: 0; padding: 0; box-sizing: border-box; }
  html, body { width: 1200px; height: 674px; overflow: hidden; background: var(--page); }
  body { position: relative; font-family: "PT Sans", Arial, sans-serif; }

  .banner { position: absolute; overflow: hidden; }
  .banner__backdrop { position: absolute; inset: 0; width: 100%; height: 100%; display: block; }
  .banner__art { position: absolute; border-radius: 10px; }
  .banner__copy { position: absolute; }
  .banner__title { font-weight: 700; white-space: nowrap; }
  .banner__tagline { font-weight: 400; }

  .banner--hero { left: 61px; top: 58px; width: 1083px; height: 348px; }
  .banner--hero .banner__art {
    left: 128px; top: 19px; width: 224px; height: 294px;
    background: linear-gradient(180deg, var(--art-printer) 0%, #1f6f9f 55%, #8fc66a 100%);
  }
  .banner--hero .banner__copy { left: 454px; top: 98px; color: var(--ink-teal); }
  .banner--hero .banner__title { font-size: 54px; line-height: 1; }
  .banner--hero .banner__tagline { font-size: 41px; line-height: 44px; margin-top: 20px; }

  .banner--small { top: 461px; width: 491px; height: 157px; }
  .banner--sky { left: 69px; }
  .banner--night { left: 651px; }
  .banner--small .banner__art {
    left: 72px; top: 8px; width: 99px; height: 133px; border-radius: 6px;
    background: linear-gradient(180deg, var(--art-printer-warm) 0%, #f0c64a 60%, #8fc66a 100%);
  }
  .banner--small .banner__copy { left: 211px; top: 41px; color: var(--label-white); }
  .banner--small .banner__title { font-size: 24px; line-height: 1; }
  .banner--small .banner__tagline { font-size: 18px; line-height: 21px; margin-top: 12px; }
  .banner--sky .banner__tagline { color: var(--sub-sky); }
  .banner--night .banner__tagline { color: var(--sub-night); }
</style>
</head>
<body>

<section class="banner banner--hero">
  <svg class="banner__backdrop" viewBox="0 0 1083 348" preserveAspectRatio="none" aria-hidden="true">
    <rect width="1083" height="348" fill="var(--sun-yellow)"/>
    <path d="M0 0 H300 C420 120 520 250 560 348 H0 Z" fill="var(--sun-orange-soft)"/>
    <path d="M0 0 H120 C240 130 300 250 320 348 H0 Z" fill="var(--sun-orange)"/>
  </svg>
  <div class="banner__art" role="img" aria-label="Flat illustration of a desktop printer printing a landscape picture"></div>
  <div class="banner__copy">
    <h1 class="banner__title">Parcel Sheet Studio</h1>
    <p class="banner__tagline">Professional Designs without<br>the headaches!</p>
  </div>
</section>

<section class="banner banner--small banner--sky">
  <svg class="banner__backdrop" viewBox="0 0 491 157" preserveAspectRatio="none" aria-hidden="true">
    <rect width="491" height="157" fill="var(--sky-blue)"/>
    <path d="M0 0 H150 C200 50 230 110 240 157 H0 Z" fill="var(--sky-mid)"/>
    <path d="M0 0 H60 C110 55 140 110 150 157 H0 Z" fill="var(--sky-teal)"/>
  </svg>
  <div class="banner__art" role="img" aria-label="Flat illustration of a desktop printer printing a landscape picture"></div>
  <div class="banner__copy">
    <h2 class="banner__title">Parcel Sheet Studio</h2>
    <p class="banner__tagline">Professional Designs without<br>the headaches!</p>
  </div>
</section>

<section class="banner banner--small banner--night">
  <svg class="banner__backdrop" viewBox="0 0 491 157" preserveAspectRatio="none" aria-hidden="true">
    <rect width="491" height="157" fill="var(--night-slate)"/>
    <path d="M0 0 H150 C200 50 230 110 240 157 H0 Z" fill="var(--night-mid)"/>
    <path d="M0 0 H60 C110 55 140 110 150 157 H0 Z" fill="var(--night-deep)"/>
  </svg>
  <div class="banner__art" role="img" aria-label="Flat illustration of a desktop printer printing a landscape picture"></div>
  <div class="banner__copy">
    <h2 class="banner__title">Parcel Sheet Studio</h2>
    <p class="banner__tagline">Professional Designs without<br>the headaches!</p>
  </div>
</section>

</body>
</html>
```